Urgent - brand new business card for a startup technical advisory and incubation business in Sydney

We need a brand new business card design for BrightForge. We are a startup technical advisory and incubation business based in Sydney Australia. We work with entrepreneurs and innovators to help rapidly and efficiently turn their ideas into reality and to ensure they have the technical platform required for growth.

Our name is partly inspired by our love of lean product development methods and the lean startup movement.

We would like clean, uncluttered designs that feature our two logo colours and communicate a professional but creative, in-touch and entrepreneurial business.

PLEASE SEE MUST HAVE PRIORITIES FOR DRAFT CONTACT INFORMATION AND OTHER DESIRED TEXT ON CARD.
Updates

We have now updated the brief to include draft business card contact information and also some additional desired text to feature on the card design.    Please review the Must Have priorities.

Also final updated source files for the horizontal and vertical versions have now been uploaded and should be used for any designs.

Thanks!

Target Market(s)

Entrepeneurs, innovators, startup investors looking for a strong product development partner

Industry/Entity Type

Business

Requirements
Must have
• Feature our two logo colours
Be a relatively clean, pared back overall design - quite minimalist

Updated source files (AI) for vertical and horizontal layouts attached.

Draft contact information for business card:
Neil Barton
Founder & CTO
Phone: +61 427 555123
Email: xxxx@brightforge.com
Skype: xxxxxbarton
Twitter: nbarton

www.brightforge.com

We would also like the overall design to include the phrase "You have great ideas. Let us make them happen." (probably in a reasonably subtle way)

Nice to have
• Inspire me! Double-sided designs are fine with logo, phrase, (URL?) on one side and contact details on other (+ any other design elements)

Logo on business card can be either with lightbulb above the wording as per example here or to the left of the BrightForge wording - both layouts in files provided.
Should not have
• Shouldn't look like a Pentara Suite business card template :-)

```html
<!DOCTYPE html>
<html lang="en">
<head>
<meta charset="utf-8">
<title>BrightForge Business Card</title>
<link rel="stylesheet" href="https://fonts.googleapis.com/css2?family=Source+Sans+3:wght@400;600;700&display=swap">
<style>
  :root {
    --stage: #858585;
    --paper: #ffffff;
    --brand-blue: #1a9ad6;
    --brand-dark: #222d38;
    --ink: #2b2b2b;
    --back-text: #f2f4f6;
  }
  * { margin: 0; padding: 0; box-sizing: border-box; }
  html, body {
    width: 996px;
    height: 1200px;
    overflow: hidden;
    background: var(--stage);
    font-family: "Source Sans 3", "Myriad Pro", sans-serif;
  }
  .canvas { position: relative; width: 996px; height: 1200px; }

  .card { position: absolute; left: 82px; width: 839px; }
  .card--front { top: 82px; height: 489px; background: var(--paper); overflow: hidden; }
  .card--back { top: 635px; height: 487px; background: var(--brand-dark); }

  .corner-square {
    position: absolute; left: 0; top: 0;
    width: 31px; height: 31px;
    background: var(--brand-blue);
  }

  .brand {
    position: absolute; left: 48px; top: 132px;
    display: flex; align-items: center; gap: 18px;
  }
  .brand__dot {
    width: 74px; height: 74px; border-radius: 50%;
    background: var(--brand-blue);
  }
  .brand__name {
    font-size: 52px; font-weight: 600; letter-spacing: -0.5px;
    color: var(--brand-dark);
    line-height: 1;
  }

  .divider {
    position: absolute; left: 472px; top: 144px;
    width: 2px; height: 214px;
    background: var(--brand-blue);
  }

  .contact { position: absolute; left: 512px; top: 136px; color: var(--ink); }
  .contact__name {
    font-size: 31px; font-weight: 700; color: var(--brand-blue); line-height: 1.1;
  }
  .contact__role { font-size: 25px; font-weight: 400; line-height: 1.2; margin-bottom: 30px; }
  .contact__list { list-style: none; font-size: 22px; line-height: 31.5px; }

  .stripes { position: absolute; left: 0; bottom: 0; }

  .website {
    position: absolute; left: 0; right: 0; top: 234px;
    text-align: center;
    font-size: 26px; font-weight: 400;
    letter-spacing: 0.45em;
    padding-left: 0.45em;
    color: var(--back-text);
  }
</style>
</head>
<body>
<main class="canvas">
  <section class="card card--front">
    <div class="corner-square"></div>

    <div class="brand">
      <span class="brand__dot"></span>
      <span class="brand__name">BrightForge</span>
    </div>

    <div class="divider"></div>

    <div class="contact">
      <h1 class="contact__name">Neil Barton</h1>
      <p class="contact__role">Founder &amp; CTO</p>
      <ul class="contact__list">
        <li>Ph: +61 427 555123</li>
        <li>Email: xxxx@brightforge.com</li>
        <li>Skype: xxxxxbarton</li>
        <li>Twitter: nbarton</li>
      </ul>
    </div>

    <svg class="stripes" width="839" height="54" viewBox="0 0 839 54" aria-hidden="true">
      <polygon points="0,20 430,20 443,34 0,34" fill="var(--brand-dark)"/>
      <polygon points="0,40 708,40 727,54 0,54" fill="var(--brand-blue)"/>
    </svg>
  </section>

  <section class="card card--back">
    <p class="website">www.brightforge.com</p>
  </section>
</main>
</body>
</html>
```